Quiet Willow Business Cards
Quiet Willow Body and Beauty Therapies
Bright & Fun-filled
Noreen Baptiste
Owner/Operator OPV, DRAM, NOPREX, VERTUMA
Bermuda
brightvanspa@examplemail.net
quietwillowvisits.com
Please design a business card with rounded corners Only the logo goes on the front. Name and additional info goes on the back Coloured background please
Noreen Baptiste (in bold print) Owner/Operator OPV, DRAM, NOPREX, VERTUMA mobile: 441-555-0148 email: brightvanspa@examplemail.net web site: quietwillowvisits.com Spa therapies in the comfort of home

```html
<!DOCTYPE html>
<html lang="en">
<head>
<meta charset="utf-8">
<title>Quiet Willow Business Cards</title>
<link href="https://fonts.googleapis.com/css2?family=Arimo:wght@400;700&display=swap" rel="stylesheet">
<style>
  :root {
    --page-bg: #ece8e2;
    --green-dark: #5c7f2a;
    --green-mid: #7da33d;
    --green-light: #a6c46a;
    --leaf: #5d8a26;
    --text-dark: #333333;
    --white: #ffffff;
    --grass: #c9d6a8;
  }
  * { margin: 0; padding: 0; box-sizing: border-box; }
  html, body {
    width: 1200px; height: 821px; overflow: hidden;
    background: var(--page-bg);
    font-family: "Arimo", Arial, sans-serif;
  }
  .canvas { position: relative; width: 1200px; height: 821px; }

  .card {
    position: absolute;
    border-radius: 24px;
    overflow: hidden;
    box-shadow: 0 6px 18px rgba(0,0,0,0.25);
  }

  /* Front */
  .card-front {
    left: 252px; top: 79px; width: 524px; height: 300px;
    background: linear-gradient(180deg, var(--green-mid) 0%, var(--green-light) 55%, var(--green-mid) 100%);
  }
  .grass-art {
    position: absolute; left: 48px; top: 58px; width: 84px; height: 150px;
    background: linear-gradient(180deg, rgba(255,255,255,0.12), var(--grass));
    border-radius: 40px 40px 12px 12px;
    opacity: 0.8;
  }
  .front-name {
    position: absolute; left: 218px; top: 78px;
    color: var(--white); font-size: 44px; font-weight: 700; line-height: 1.05;
  }
  .front-tagline {
    position: absolute; left: 144px; top: 194px;
    color: var(--white); font-size: 18px; font-weight: 400;
  }

  /* Back */
  .card-back {
    left: 444px; top: 413px; width: 528px; height: 360px;
    background: var(--white);
  }
  .holder-name {
    position: absolute; left: 30px; top: 30px;
    color: var(--leaf); font-size: 27px; font-weight: 700;
  }
  .credentials {
    position: absolute; left: 30px; top: 66px;
    color: var(--text-dark); font-size: 11px;
  }
  .contact {
    position: absolute; left: 30px; top: 200px;
    color: var(--text-dark); font-size: 12px; line-height: 17px;
    list-style: none;
  }
  .back-name {
    position: absolute; right: 22px; top: 146px;
    color: var(--leaf); font-size: 34px; font-weight: 700; line-height: 1;
    text-align: right;
  }
  .back-tagline {
    position: absolute; right: 22px; top: 222px;
    color: var(--leaf); font-size: 11px;
  }
  .web-band {
    position: absolute; left: 0; bottom: 0; width: 100%; height: 112px;
    background: linear-gradient(180deg, var(--green-light) 0%, var(--green-mid) 35%, var(--green-dark) 100%);
  }
  .website {
    position: absolute; left: 0; top: 14px; width: 100%;
    text-align: center; color: var(--white); font-size: 16px;
  }
</style>
</head>
<body>
<main class="canvas">
  <section class="card card-front" aria-label="Card front">
    <div class="grass-art" role="img" aria-label="Illustration of a tuft of grass with flowers and pearls"></div>
    <div class="front-name">Quiet<br>Willow</div>
    <div class="front-tagline">Mobile Body &amp; Beauty Therapies</div>
  </section>

  <section class="card card-back" aria-label="Card back">
    <h1 class="holder-name">Noreen Baptiste</h1>
    <p class="credentials">Owner/Operator OPV, DRAM, NOPREX, VERTUMA</p>
    <ul class="contact">
      <li>M: 441-555-0148</li>
      <li>E: brightvanspa@examplemail.net</li>
    </ul>
    <div class="back-name">Quiet<br>Willow</div>
    <div class="back-tagline">Mobile Body &amp; Beauty Therapies</div>
    <div class="web-band">
      <p class="website">quietwillowvisits.com</p>
    </div>
  </section>
</main>
</body>
</html>
```